Expanding Agricultural services business needs a brochure in booklet style design

I currently have a small ag services business. We have been in business for 20 years. We now offer soil sampling and soil testing. we are expanding to offer new services which are fieldora seed sales and seed treatment. we want to get the word out about our expansion.....what we are offering......give brief detail about each service .......and let customers know that we are offering a "bundle" package to increase their productivity with a customer bonus reward program to earn free Farm Drainage Tiling.
Updates

Hello All,

Somehow my uploads of pictures and text did not end up on my project.  I have added back my pictures and in a couple hours will have text added.  Thank you for your patience!

Norma

Would like this brochure in booklet style.....but if you think it would be better in another style....im open to about anything!

Thanks in advance

Hello again folks!

I have added my text.....and pix......sorry for the inconvenience

                                       

As it turns out......it seems 4 pages is not enought to get all my information out.  I believe I would like to stress the FENWICK AG SERVICES EXPANSION 2013 .   We have offered soil testing services for 20 years and are expanding to offer Fieldora Seed  Sales and a new seed treatment facility.  We are putting together a Productivity Bundle......for increased yields, plus the opportunity to earn Drainage Tiling credits towards FREE Drainage Tiling.

It does not matter to me how many pages this ends up being.....I just need to get all my information in this booklet.

Thanks sooooo much

 

I must be able to edit my brochure after download.  It will need to be in an editable format.

Thanks

Target Market(s)

farmers

Industry/Entity Type

Business

Requirements
Must have
• I must be able to edit the brochure myself after download. So it will need to be in an editable format.
Nice to have
• farm related items...tractor...crops.....etc.

```html
<!DOCTYPE html>
<html lang="en">
<head>
<meta charset="utf-8">
<title>Fenwick Ag Services Expansion Booklet</title>
<link href="https://fonts.googleapis.com/css2?family=Oswald:wght@300;400;500&family=Montserrat:wght@700&family=Open+Sans:wght@400;600;700&family=Quicksand:wght@400&display=swap" rel="stylesheet">
<style>
  :root{
    --stage:#2b2b2b;
    --olive:#bfb524;
    --olive-text:#d9d22e;
    --earth:#2f2a24;
    --paper:#ffffff;
    --paper-grey:#f1f1f1;
    --ink:#3a342c;
    --ink-soft:#8a8a8a;
    --label:#f2f2f2;
    --pale:#cfcac1;
  }
  *{box-sizing:border-box;margin:0;padding:0}
  html,body{width:1200px;height:900px;overflow:hidden;background:var(--stage)}
  body{position:relative;font-family:"Open Sans",sans-serif}
  .view-label{position:absolute;font-family:"Quicksand",sans-serif;color:var(--label);font-size:30px;letter-spacing:1px}
  .page{position:absolute;overflow:hidden}
  .photo{display:block;width:100%}
  .body-copy{font-size:3.4px;line-height:1.35;text-align:justify}
  .body-copy h4{font-size:3.8px;font-weight:700;margin:3px 0 1px}
  .band-title{font-family:"Oswald",sans-serif;font-weight:300;text-transform:uppercase}

  /* page 1 */
  .p-cost{left:99px;top:79px;width:187px;height:242px;background:var(--paper)}
  .p-cost .header{height:30px;background:var(--olive);color:#fff;font-size:13px;padding:6px 10px;line-height:18px}
  .p-cost .photo{height:125px;background:radial-gradient(circle at 50% 50%,#6b4a32 0%,#2d1e14 70%)}
  .p-cost .body-copy{color:var(--ink);padding:24px 10px 0}

  /* page 2 */
  .p-drain{left:287px;top:79px;width:187px;height:242px;background:var(--earth);color:#d8d4cc}
  .p-drain .title{padding:7px 30px 0;font-size:10px;line-height:1;color:#fff;font-weight:400}
  .p-drain .title strong{display:block;font-size:7px;font-weight:700;margin-top:2px}
  .p-drain .body-copy{padding:0 30px;color:#c9c4bb}
  .p-drain .body-copy h4{color:#fff}
  .p-drain .photo-wrap{position:absolute;left:0;top:131px;width:187px;height:111px}
  .p-drain .photo{height:111px;background:linear-gradient(180deg,#c8cfc0 0%,#8e9b6c 45%,#3a3024 100%)}
  .p-drain .diagram{position:absolute;right:5px;top:0;width:60px;height:44px;background:#f4f6ef}

  /* page 3 */
  .p-seed{left:99px;top:322px;width:187px;height:243px;background:var(--paper)}
  .p-seed .photo{height:115px;background:radial-gradient(circle at 50% 40%,#5a4636 0%,#241a13 75%)}
  .p-seed .header{height:23px;background:var(--earth);color:#e8e4dc;font-size:6px;line-height:8px;padding:8px 6px 0;letter-spacing:.2px}
  .p-seed .detail{display:flex;gap:4px;padding:8px 4px 0 5px}
  .p-seed .thumb{flex:0 0 62px;height:86px;background:linear-gradient(180deg,#c9a26a 0%,#7a5a32 60%,#3c2c1a 100%)}
  .p-seed .body-copy{color:var(--ink);flex:1}
  .p-seed .body-copy h4{margin-top:0}

  /* page 4 */
  .p-corn{left:287px;top:322px;width:187px;height:243px;background:var(--paper-grey)}
  .p-corn .photo-wrap{position:relative;height:46px}
  .p-corn .photo{height:46px;background:linear-gradient(90deg,#4f8a2a 0%,#7fb237 30%,#f0c23a 55%,#e8a820 100%)}
  .p-corn .brand{position:absolute;left:18px;top:6px;color:#fff;font-size:7px;font-weight:700;line-height:1}
  .p-corn .brand span{display:block;text-align:right;font-size:4px;font-weight:600}
  .p-corn .body-copy{color:var(--ink-soft);padding:10px 10px 0}

  /* page 5 */
  .p-soy{left:99px;top:568px;width:187px;height:240px;background:var(--olive)}
  .p-soy .photo-wrap{position:relative;height:56px}
  .p-soy .photo{height:56px;background:linear-gradient(160deg,#2f6a1d 0%,#5a9a32 50%,#e8e2c6 100%)}
  .p-soy .brand{position:absolute;left:53px;top:19px;color:#fff;font-size:13px;font-weight:700}
  .p-soy .body-copy{color:var(--ink);padding:6px 13px 0}
  .p-soy .intro.body-copy{height:36px;background:var(--earth);color:var(--pale);padding:7px 13px 0}

  /* back */
  .p-back{left:287px;top:568px;width:187px;height:240px;background:var(--earth)}
  .p-back .band{position:absolute;left:0;top:93px;width:100%;height:39px;background:var(--olive)}
  .p-back .contact{position:absolute;top:183px;width:100%;text-align:center;color:#fff;font-size:4.5px;font-weight:700;line-height:1.3}
  .p-back .company{position:absolute;top:210px;width:100%;text-align:center;color:#fff;font-size:5px;font-weight:700;letter-spacing:.3px}

  /* cover */
  .p-cover{left:690px;top:290px;width:270px;height:350px;background:var(--earth)}
  .p-cover .photo{height:136px;background:linear-gradient(180deg,#8a9a3a 0%,#6f8a2a 40%,#3f5a18 100%)}
  .p-cover .band{height:56px;background:var(--olive);color:#fff;font-family:"Montserrat",sans-serif;font-size:10px;line-height:14px;padding:14px 30px 0}
  .p-cover .section{padding:87px 10px 0 14px}
  .p-cover .section h3{color:var(--olive-text);font-size:11px;line-height:1;margin-bottom:3px;font-weight:400}
  .p-cover .section p{color:#e6e2da;font-size:5px;line-height:1.3;text-align:justify}
</style>
</head>
<body>
  <div class="view-label" style="left:113px;top:40px">insides</div>
  <div class="view-label" style="left:502px;top:715px;font-size:36px">back</div>
  <div class="view-label" style="left:805px;top:668px">cover</div>

  <section class="page p-cost">
    <div class="header band-title">Cost Reduction</div>
    <div class="photo" role="img" aria-label="Cupped hands holding dark soil with a young seedling"></div>
    <p class="body-copy">Soil test reports will provide you with appropriate fertilizer application recommendations for nitrogen, phosphorus, potassium and limestone. If you apply too little fertilizer, your crop yields and returns will be lower. Too much fertilizer will waste time and money and risk environmental damage due to nutrient runoff. Consequently, soil testing provides a farm management tool with a potential benefit to the farmer of increased yields, reduced operating costs and a good environmental risk management.</p>
  </section>

  <section class="page p-drain">
    <h2 class="title">Benefits of<strong>Farm Drainage</strong></h2>
    <div class="body-copy">
      <h4>Higher Crop Yields</h4>
      <p>Farm drainage increases your crop yields by making sure your crops get the right amount of moisture through the growing season. When spring rains saturate your soil, a good drainage system will remove excess water and lower the water table. Warmer soil helps seed germination and reduces disease.</p>
      <h4>Cost Reduction</h4>
      <p>Farm drainage reduces cropping costs by ensuring the best yields for your investment. It removes the need to replant and lets you plant earlier in the spring.</p>
      <h4>Increased Farm Value</h4>
      <p>If you view your farmland as an investment, drainage tiling will pay you back year after year.</p>
    </div>
    <div class="photo-wrap">
      <div class="photo" role="img" aria-label="Young corn sprout rising from a field"></div>
      <div class="diagram" role="img" aria-label="Diagram of drainage tile lowering the water table below plant roots"></div>
    </div>
  </section>

  <section class="page p-seed">
    <div class="photo" role="img" aria-label="Hands planting seeds into tilled soil"></div>
    <div class="header band-title">Benefits of Seed Treatments</div>
    <div class="detail">
      <div class="thumb" role="img" aria-label="Combine harvester in a grain field"></div>
      <div class="body-copy">
        <h4>HIGHER CROP YIELDS</h4>
        <p>Wet, poorly drained soils are typical during spring planting and crop emergence. These conditions favor fungal pathogens that cause seedling diseases which can slow germination and plant growth. Seed treatments can help protect seed and seedlings from pests, resulting in more uniform stands, better yield potential and ultimately increased return on investment.</p>
      </div>
    </div>
  </section>

  <section class="page p-corn">
    <div class="photo-wrap">
      <div class="photo" role="img" aria-label="Close view of a ripe yellow ear of corn"></div>
      <div class="brand">Amber Reach<span>Corn</span></div>
    </div>
    <div class="body-copy">
      <p>Corn is one of the most productive crops grown each year, and you get over 500 kernels in return. Amber Reach hybrids are bred for strong stands across many soil types and seasons.</p>
      <h4 style="margin-top:18px">Germplasm diversity</h4>
      <p>Our germplasm portfolio draws on a wide range of breeding programs to deliver hybrids that stay strong under drought, disease and pest pressure across every region we serve.</p>
      <h4>Innovation in biotechnology</h4>
      <p>Traits stacked into our hybrids protect the plant above and below ground, so growers can focus on yield and profit instead of insects and weeds. We keep investing in new traits each season.</p>
    </div>
  </section>

  <section class="page p-soy">
    <p class="intro body-copy">First grown in East Asia more than 1,000 years ago, soybean is today the world's primary source of protein and edible oil.</p>
    <div class="photo-wrap">
      <div class="photo" role="img" aria-label="Rows of green soybean plants in a field"></div>
      <div class="brand">fieldora</div>
    </div>
    <div class="body-copy">
      <p>Today, more than 260 million tons of soybean are harvested each year, with most grown in just a few countries. Demand keeps rising as soybean remains a key source of quality protein.</p>
      <h4>Crop health</h4>
      <p>Pests and diseases can cut soybean yields sharply. Good seed, sound crop rotation and careful field scouting keep plants healthy through the season.</p>
      <h4>Integrated offers for soybean growers</h4>
      <p>Fieldora combines strong genetics, seed treatments and crop protection into one plan designed to help growers get the most from every acre.</p>
    </div>
  </section>

  <section class="page p-back">
    <div class="band"></div>
    <p class="contact">your contact info<br>goes here</p>
    <p class="company">FENWICK AG SERVICES</p>
  </section>

  <section class="page p-cover">
    <div class="photo" role="img" aria-label="Hand brushing through green wheat heads"></div>
    <h1 class="band">CROP HEALTH CONCENTRATION<br>CROP YIELD DOMINATION!</h1>
    <div class="section">
      <h3 class="band-title">Soil Testing</h3>
      <p>The practice and use of soil testing has become widely accepted in agri-business both by farmers and industry. The potential for increased yields and profits has been the obvious motivator for the keen interest in soil testing.</p>
    </div>
  </section>
</body>
</html>
```